CrestHornSupply.com

I need a new webdesign for a company in the San Jose/SF Bay area that showcases the financial benefits of buying used band instruments for junior high students.This would be opposed to the current and costly option of renting cheap quality instruments from the 2 or 3 local music stores that charge a monthly fee that over the years charges the buyer 3 or 4x over..
Instruments: focus in on Alto Sax, Trumpet, Flute, Clarinet, Trombone, Tenor Sax, Baritone
Target middle schools are Willowmere Middle School and Harlan Middle School in San Jose, CA. Both have award winning band programs.
Files attached may or may not be important.
Tabs Needed and funtional
Contact
Shopping Cart
Select Instrument
Checkout
Add to Cart, etc.
Instuments
quantity, etc.
trade in your instrument/sell your instrument
ability to add or take away new instruments for sale. including pictures
Additional questions or info, feel free to ask
Updates
Hi Designers,
Project Deadline Extended
Reason: In the next week you will be receiving specific content that will be required to be had on the website.
New desigins are still welcome. Please continue to contact me if you have questions about your individual designs.
Thanks!
Crest Horn

```html
<!DOCTYPE html>
<html lang="en">
<head>
<meta charset="utf-8">
<title>Crest Horn — Used Band Instruments</title>
<link rel="stylesheet" href="https://fonts.googleapis.com/css2?family=Alfa+Slab+One&family=Arimo:wght@400;700&display=swap">
<style>
  :root {
    --red: #e8141b;
    --red-dark: #9c0d10;
    --ink: #1b1b1b;
    --page-dark: #161616;
    --wall: #2b2b2b;
    --panel: #f4f4f4;
    --white: #ffffff;
    --text-grey: #6b6b6b;
    --footer: #2a2a2a;
    --footer-line: #454545;
    --footer-link: #8a8a8a;
    --nav: #262626;
  }
  * { box-sizing: border-box; margin: 0; padding: 0; }
  html, body { width: 953px; height: 1200px; overflow: hidden; }
  body {
    position: relative;
    font-family: "Arimo", Arial, sans-serif;
    background: linear-gradient(180deg, #2e2e2e 0%, #242424 45%, #0c0c0c 85%, #000 100%);
    color: var(--ink);
  }
  .slab { font-family: "Alfa Slab One", "Arimo", serif; font-weight: 400; }

  /* header */
  .logo {
    position: absolute; left: 140px; top: 38px;
    display: flex; align-items: center; gap: 8px;
  }
  .logo-mark { width: 12px; height: 12px; background: var(--red); }
  .logo-name { font-size: 34px; line-height: 34px; color: var(--white); width: 130px; }

  .currency { position: absolute; top: 26px; right: 100px; display: flex; gap: 3px; }
  .currency span {
    width: 12px; height: 12px; font-size: 8px; font-weight: 700; line-height: 12px;
    text-align: center; background: #444; color: var(--white);
  }
  .currency span.active { background: var(--red); }

  .cart-bar {
    position: absolute; left: 632px; top: 52px; width: 221px; height: 21px;
    background: #333; font-size: 9px; line-height: 21px; padding-left: 14px; color: #bbb;
  }
  .cart-bar b { color: var(--red); font-weight: 700; }
  .cart-bar .caret { position: absolute; right: 10px; top: 9px; border: 3px solid transparent; border-top-color: #ccc; }

  .top-links { position: absolute; right: 100px; top: 84px; font-size: 9px; display: flex; gap: 10px; color: #9a9a9a; }
  .top-links .accent { color: var(--red); }

  .search {
    position: absolute; left: 534px; top: 108px; width: 319px; height: 39px;
    background: var(--red); display: flex; align-items: center;
  }
  .search-label { color: var(--white); font-size: 17px; padding: 0 8px 0 12px; }
  .search-field {
    flex: 1; height: 30px; background: var(--red-dark); color: #e87070;
    font-size: 8px; line-height: 30px; padding-left: 11px; margin-right: 5px; position: relative;
  }
  .search-btn { position: absolute; right: 5px; top: 4px; width: 22px; height: 22px; background: var(--red); }

  /* nav */
  .main-nav {
    position: absolute; left: 99px; top: 148px; width: 754px; height: 40px;
    background: var(--nav); display: flex;
  }
  .main-nav a {
    color: var(--white); text-decoration: none; font-size: 10.5px; font-weight: 700;
    line-height: 40px; padding: 0 16px; border-right: 1px solid #151515;
  }
  .main-nav a:first-child { padding-left: 16px; }
  .main-nav a:last-child { border-right: 0; }

  /* hero */
  .hero {
    position: absolute; left: 99px; top: 188px; width: 754px; height: 415px;
    background: radial-gradient(ellipse at 55% 55%, #4a3a30 0%, #2a1f1c 45%, #140f0f 100%);
  }
  .slider-dots {
    position: absolute; right: 15px; bottom: 14px; width: 46px; height: 16px;
    background: var(--red); display: flex; justify-content: center; align-items: center; gap: 4px;
  }
  .slider-dots i { width: 8px; height: 8px; border-radius: 50%; background: var(--white); }
  .slider-dots i.current { background: #2a2a2a; }

  .to-top { position: absolute; left: 902px; top: 556px; }

  /* content panel */
  .content {
    position: absolute; left: 99px; top: 603px; width: 754px; height: 414px; background: var(--white);
  }
  .content::before { content: ""; position: absolute; left: 0; top: 0; width: 754px; height: 98px; background: var(--panel); }

  .sale-banner {
    position: absolute; left: 14px; top: 16px; width: 456px; height: 68px;
    background: #1d1d1d; display: flex; align-items: center;
  }
  .sale-word { color: var(--white); font-size: 52px; line-height: 1; padding: 0 10px 0 14px; }
  .sale-head { font-size: 25px; line-height: 1; color: #777; }
  .sale-head .white { color: var(--white); }
  .sale-head .red { color: var(--red); }
  .sale-copy { font-size: 7.5px; line-height: 12px; color: #bdbdbd; margin-top: 4px; }

  .ship-banner {
    position: absolute; left: 484px; top: 16px; width: 256px; height: 68px;
    background: var(--red); color: var(--white); text-align: center; padding-top: 10px;
  }
  .ship-banner h3 { font-size: 22px; line-height: 1; font-weight: 400; }
  .ship-banner p { font-size: 10px; font-weight: 700; margin-top: 2px; }
  .ship-banner small { display: block; font-size: 7.5px; }

  .section-title {
    position: absolute; left: 14px; top: 97px; width: 726px; height: 21px;
    border-bottom: 2px solid #e1e1e1; font-size: 12px; font-weight: 700;
  }
  .section-title .red { color: var(--red); }
  .section-arrows { position: absolute; right: 0; top: 2px; display: flex; gap: 6px; }

  .products { position: absolute; left: 14px; top: 136px; width: 726px; display: flex; gap: 14px; }
  .product { width: 171px; }
  .product-media { height: 125px; border-radius: 4px; }
  .m-brass { background: radial-gradient(ellipse at center, #caa04e 0%, #e9d7ae 40%, #fff 70%); }
  .m-drums { background: radial-gradient(ellipse at center, #6b1c25 0%, #c9c2c2 40%, #fff 70%); }
  .m-uke { background: radial-gradient(ellipse at center, #a86a2a 0%, #e6cdb0 40%, #fff 70%); }
  .m-keys { background: radial-gradient(ellipse at center, #555 0%, #c8c8c8 40%, #fff 70%); }
  .product-name {
    margin-top: 28px; height: 38px; border-bottom: 1px solid #e4e4e4;
    font-size: 8.5px; font-weight: 700; line-height: 13px; color: var(--red); text-transform: uppercase;
  }
  .product-desc { margin-top: 12px; font-size: 8.5px; line-height: 13px; color: var(--text-grey); }
  .product-buy { margin-top: 10px; display: flex; align-items: center; }
  .price { font-size: 12px; font-weight: 700; width: 70px; }
  .add-to-cart {
    width: 76px; height: 24px; background: var(--red); color: var(--white);
    font-size: 8.5px; line-height: 24px; text-align: center;
  }

  /* footer */
  .site-footer {
    position: absolute; left: 99px; top: 1017px; width: 754px; height: 161px; background: var(--footer);
  }
  .footer-cols { position: absolute; left: 14px; top: 20px; display: flex; gap: 14px; }
  .footer-col { width: 171px; }
  .footer-col h4 {
    color: var(--white); font-size: 10px; font-weight: 700; height: 17px;
    border-bottom: 1px solid var(--footer-line); margin-bottom: 9px;
  }
  .footer-col li { list-style: none; font-size: 8.5px; font-weight: 700; color: var(--footer-link); line-height: 14.2px; }
  .footer-col li::before { content: "› "; color: var(--red); }
  .footer-rule { position: absolute; left: 14px; top: 119px; width: 726px; height: 1px; background: var(--footer-line); }
  .copyright { position: absolute; left: 15px; top: 132px; font-size: 8.5px; color: #777; }
</style>
</head>
<body>

<header>
  <div class="logo">
    <span class="logo-mark"></span>
    <span class="logo-name slab">CREST HORN</span>
  </div>
  <div class="currency"><span>€</span><span>£</span><span class="active">$</span></div>
  <div class="cart-bar"><b>SHOPPING CART :</b> 0 item(s) - $0.00<span class="caret"></span></div>
  <nav class="top-links">
    <span>Wish list (0)</span><span>My account</span><span>Shopping cart</span><span>Checkout</span>
    <span class="accent">Login</span><span class="accent">Create an account</span>
  </nav>
  <div class="search">
    <span class="search-label slab">SEARCH</span>
    <div class="search-field">Enter search keywords here
      <span class="search-btn">
        <svg width="22" height="22" viewBox="0 0 22 22"><circle cx="10" cy="10" r="4" fill="none" stroke="#fff" stroke-width="1.8"/><line x1="13" y1="13" x2="16" y2="16" stroke="#fff" stroke-width="2"/></svg>
      </span>
    </div>
  </div>
</header>

<nav class="main-nav">
  <a href="#">ALTO SAX</a><a href="#">TRUMPET</a><a href="#">FLUTE</a><a href="#">CLARINET</a>
  <a href="#">TROMBONE</a><a href="#">TENOR SAX</a><a href="#">BARITONE</a>
</nav>

<section class="hero" role="img" aria-label="Young band members playing guitars together on a dark stage">
  <div class="slider-dots"><i></i><i class="current"></i><i></i></div>
</section>

<svg class="to-top" width="26" height="16" viewBox="0 0 26 16"><polyline points="2,14 13,4 24,14" fill="none" stroke="#fff" stroke-width="3"/></svg>

<main class="content">
  <div class="sale-banner">
    <span class="sale-word slab">SALE</span>
    <div>
      <div class="sale-head slab">UP TO <span class="white">70%</span> <span class="red">OFF</span></div>
      <p class="sale-copy">LOREM IPSUM DOLOR SIT AMET CONSE CTETUR ADIPISICING ELIT, SED DO<br>EIUSMOD TEMPOR INCIDIDUNT UT LABORE ET DOLORE.</p>
    </div>
  </div>
  <div class="ship-banner">
    <h3 class="slab">FREE SHIPPING</h3>
    <p>ON ORDERS OVER $ 499.</p>
    <small>This offer is valid on all our store items</small>
  </div>

  <h2 class="section-title">USED BAND <span class="red">INSTRUMENTS</span>
    <span class="section-arrows">
      <svg width="6" height="9" viewBox="0 0 6 9"><polygon points="6,0 0,4.5 6,9" fill="#777"/></svg>
      <svg width="6" height="9" viewBox="0 0 6 9"><polygon points="0,0 6,4.5 0,9" fill="#111"/></svg>
    </span>
  </h2>

  <div class="products">
    <article class="product">
      <div class="product-media m-brass" role="img" aria-label="Brass flugelhorn"></div>
      <h3 class="product-name">Lorem ipsum dolor sit amet conse ctetur</h3>
      <p class="product-desc">Our store is one of the best among the variety of the competing ones....</p>
      <div class="product-buy"><span class="price">$90.00</span><span class="add-to-cart">ADD TO CART</span></div>
    </article>
    <article class="product">
      <div class="product-media m-drums" role="img" aria-label="Red drum kit with cymbals"></div>
      <h3 class="product-name">Labore et dolore magna</h3>
      <p class="product-desc">Our store is one of the best among the variety of the competing ones....</p>
      <div class="product-buy"><span class="price">$90.00</span><span class="add-to-cart">ADD TO CART</span></div>
    </article>
    <article class="product">
      <div class="product-media m-uke" role="img" aria-label="Wooden ukulele"></div>
      <h3 class="product-name">Ipsum dolor conse</h3>
      <p class="product-desc">Our store is one of the best among the variety of the competing ones....</p>
      <div class="product-buy"><span class="price">$90.00</span><span class="add-to-cart">ADD TO CART</span></div>
    </article>
    <article class="product">
      <div class="product-media m-keys" role="img" aria-label="Electronic keyboard"></div>
      <h3 class="product-name">Magna aliqua.</h3>
      <p class="product-desc">Our store is one of the best among the variety of the competing ones....</p>
      <div class="product-buy"><span class="price">$400.00</span><span class="add-to-cart">ADD TO CART</span></div>
    </article>
  </div>
</main>

<footer class="site-footer">
  <div class="footer-cols">
    <div class="footer-col"><h4>INFORMATION</h4><ul><li>About</li><li>Delivery</li><li>Privacy Policy</li><li>Terms &amp; Conditions</li></ul></div>
    <div class="footer-col"><h4>CUSTOMER SERVICE</h4><ul><li>Contact Us</li><li>Returns</li><li>Site Map</li></ul></div>
    <div class="footer-col"><h4>EXTRAS</h4><ul><li>Brands</li><li>Gift Vouchers</li><li>Affiliates</li><li>Specials</li></ul></div>
    <div class="footer-col"><h4>MY ACCOUNT</h4><ul><li>My Account</li><li>Order History</li><li>Wish List</li><li>Newsletter</li></ul></div>
  </div>
  <div class="footer-rule"></div>
  <p class="copyright">Copyright © 2014 cresthorn. All Right Reserved</p>
</footer>

</body>
</html>
```